" Somos um eccomerce de iluminação led. temos um portfólio muito vasto de produtos para atender diversas demandas: consumidor final, revenda, condomínios e empresas no modo geral. "

```html
<!DOCTYPE html>
<html lang="pt-BR">
<head>
<meta charset="utf-8">
<title>Refletor LED – Catálogo 2018</title>
<link rel="stylesheet" href="https://fonts.googleapis.com/css2?family=Open+Sans:wght@400;600;700;800&display=swap">
<style>
  :root{
    --stage:#d6d6d6;
    --paper:#ffffff;
    --ink:#3a3a3a;
    --ink-soft:#6b6b6b;
    --teal:#3f9aa0;
    --teal-dark:#2f7f85;
    --row:#f1f1f1;
    --row-alt:#e7e7e7;
    --icon:#444;
  }
  *{box-sizing:border-box;margin:0;padding:0}
  html,body{width:1200px;height:1200px;overflow:hidden}
  body{background:var(--stage);font-family:"Open Sans",Arial,sans-serif;color:var(--ink);position:relative}
  .spread{position:absolute;left:30px;top:197px;width:1140px;height:806px;display:flex;box-shadow:0 10px 30px rgba(0,0,0,.25)}
  .page{position:relative;width:570px;height:806px;background:var(--paper);overflow:hidden}
  .page--left{background:linear-gradient(90deg,#fff 88%,#ececec 100%)}
  .page--right{background:linear-gradient(90deg,#ececec 0%,#fff 10%)}
  .hero{position:absolute;left:0;top:0;width:100%;height:115px}
  .page--left .hero{background:linear-gradient(90deg,#cfd6db,#eef1f3 45%,#dfe5e8)}
  .page--right .hero{background:linear-gradient(90deg,#c9d0d3,#f2f4f5 40%,#b9c3c7 75%,#e3e8ea)}
  .side-tab{position:absolute;right:0;top:115px;width:24px;height:220px;background:var(--teal);display:flex;align-items:center;justify-content:center}
  .side-tab span{writing-mode:vertical-rl;color:#fff;font-size:9px;font-weight:600;letter-spacing:.3px;white-space:nowrap}
  .side-tab b{font-weight:800}
  .folio{position:absolute;bottom:26px;font-size:11px;color:var(--ink-soft)}
  .page--left .folio{left:40px}
  .page--right .folio{left:40px}

  .product{position:absolute;left:0;width:100%}
  .product--top{top:138px}
  .product--bottom{top:478px}
  .product__head{position:absolute;left:90px;top:0;right:40px;height:40px;display:flex;align-items:center}
  .product__title{font-size:26px;font-weight:700;letter-spacing:-.3px;color:var(--ink);width:170px}
  .product__tag{flex:1;height:40px;position:relative}
  .product__tag span{position:absolute;left:0;top:6px;width:190px;height:26px;background:var(--teal);color:#fff;font-size:14px;font-weight:600;display:flex;align-items:center;justify-content:center;border-radius:2px}
  .product__tag::after{content:"";position:absolute;left:0;right:0;bottom:6px;height:2px;background:var(--teal)}
  .product__ref{position:absolute;left:62px;top:78px;font-size:8px;color:var(--ink-soft)}
  .product__image{position:absolute;left:60px;top:92px;width:140px;height:120px;border-radius:4px}
  .badges{position:absolute;left:232px;top:58px;display:flex;gap:22px}
  .badge{display:flex;align-items:center;gap:6px;font-size:10px;font-weight:700;line-height:1.15;color:var(--ink)}
  .badge__icon{width:16px;height:18px;background:var(--icon);border-radius:2px;flex:none}
  .specs{position:absolute;left:232px;top:96px;width:290px;border-collapse:separate;border-spacing:0 3px;font-size:9.5px}
  .specs th,.specs td{height:21px;padding:0 10px;text-align:left;background:var(--row)}
  .specs th{width:95px;font-weight:400;color:var(--ink-soft);background:var(--row-alt)}
  .specs td{color:var(--ink)}
</style>
</head>
<body>
<div class="spread">

  <section class="page page--left">
    <div class="hero" role="img" aria-label="Foto de ambiente interno iluminado com luz branca"></div>

    <article class="product product--top">
      <header class="product__head"><h2 class="product__title">Refletor LED</h2><div class="product__tag"><span>Recarregável</span></div></header>
      <div class="badges">
        <div class="badge"><i class="badge__icon"></i>Garantia<br>de 1 ano</div>
        <div class="badge"><i class="badge__icon"></i>Índice de<br>Proteção IP 66</div>
        <div class="badge"><i class="badge__icon"></i>Vida Útil de<br>50.000 horas</div>
      </div>
      <p class="product__ref">Ref. 013</p>
      <div class="product__image" role="img" aria-label="Foto do refletor LED recarregável amarelo e preto" style="background:radial-gradient(circle at 50% 50%,#f2c21b 0 30%,#3a3a3a 31% 45%,#fff 46%)"></div>
      <table class="specs">
        <tr><th>Potência</th><td>10w, 20w, 30w</td></tr>
        <tr><th>Cor da Luz</th><td>Branco Frio</td></tr>
        <tr><th>Fator Potência</th><td>&gt; 0,9</td></tr>
        <tr><th>Lúmens</th><td>900, 2400, 2600</td></tr>
        <tr><th>Voltagem</th><td>110v - 220v</td></tr>
      </table>
    </article>

    <article class="product product--bottom">
      <header class="product__head"><h2 class="product__title">Refletor LED</h2><div class="product__tag"><span>Performance</span></div></header>
      <div class="badges">
        <div class="badge"><i class="badge__icon"></i>Garantia<br>de 3 anos</div>
        <div class="badge"><i class="badge__icon"></i>Índice de<br>Proteção IP 66</div>
        <div class="badge"><i class="badge__icon"></i>Vida Útil de<br>50.000 horas</div>
      </div>
      <p class="product__ref">Ref. 014</p>
      <div class="product__image" role="img" aria-label="Foto do refletor LED performance prateado" style="background:linear-gradient(180deg,#e4e7e9,#b9bfc4)"></div>
      <table class="specs">
        <tr><th>Potência</th><td>30w, 50w, 100w, 150w, 200w</td></tr>
        <tr><th>Cor da Luz</th><td>Branco Frio</td></tr>
        <tr><th>Fator Potência</th><td>&gt; 0,9</td></tr>
        <tr><th>Lúmens</th><td>2800, 3400, 14000, 18000, 18000</td></tr>
        <tr><th>Voltagem</th><td>110v - 220v</td></tr>
      </table>
    </article>

    <p class="folio">09</p>
  </section>

  <section class="page page--right">
    <div class="hero" role="img" aria-label="Foto de sala moderna com iluminação LED"></div>
    <div class="side-tab"><span><b>Refletores LED</b> | Catálogo 2018</span></div>

    <article class="product product--top">
      <header class="product__head"><h2 class="product__title">Refletor LED</h2><div class="product__tag"><span>Prismático</span></div></header>
      <div class="badges">
        <div class="badge"><i class="badge__icon"></i>Garantia<br>de 1 ano</div>
        <div class="badge"><i class="badge__icon"></i>Índice de<br>Proteção IP 66</div>
        <div class="badge"><i class="badge__icon"></i>Vida Útil de<br>50.000 horas</div>
      </div>
      <p class="product__ref">Ref. 015</p>
      <div class="product__image" role="img" aria-label="Foto do refletor LED prismático preto" style="background:radial-gradient(circle,#f4f4f4 0 38%,#2a2a2a 39% 50%,#fff 51%)"></div>
      <table class="specs">
        <tr><th>Potência</th><td>10w, 20w, 30w, 50w</td></tr>
        <tr><th>Cor da Luz</th><td>Branco Frio, Branco Quente</td></tr>
        <tr><th>Fator Potência</th><td>&gt; 0,9</td></tr>
        <tr><th>Lúmens</th><td>900, 1800, 2700, 4500</td></tr>
        <tr><th>Voltagem</th><td>110v - 220v</td></tr>
      </table>
    </article>

    <article class="product product--bottom">
      <header class="product__head"><h2 class="product__title">Refletor LED</h2><div class="product__tag"><span>Espeto</span></div></header>
      <div class="badges">
        <div class="badge"><i class="badge__icon"></i>Garantia<br>de 1 ano</div>
        <div class="badge"><i class="badge__icon"></i>Índice de<br>Proteção IP 65</div>
        <div class="badge"><i class="badge__icon"></i>Vida Útil de<br>50.000 horas</div>
      </div>
      <p class="product__ref">Ref. 016</p>
      <div class="product__image" role="img" aria-label="Foto do refletor LED de espeto para jardim" style="background:radial-gradient(circle at 40% 35%,#b8e05a 0 10%,#1e1e1e 11% 28%,#fff 29%)"></div>
      <table class="specs">
        <tr><th>Potência</th><td>3,5w, 3w, 5w, 7w</td></tr>
        <tr><th>Cor da Luz</th><td>Branco Frio, Verde, Vermelho, Âmbar, Azul</td></tr>
        <tr><th>Fator Potência</th><td>&gt; 0,9</td></tr>
        <tr><th>Ângulo Abertura</th><td>30°</td></tr>
        <tr><th>Voltagem</th><td>110v - 220v</td></tr>
      </table>
    </article>

    <p class="folio">10</p>
  </section>

</div>
</body>
</html>
```